Thank You Card

Catering company customer Thank You cards

Thank you card to past clients after event completion

Should be on recycled or green paper.

Room to write personal message. No long prewritten messages of thanks and gratitude.

Should have Red and Zapfino fonts to match logo

Simple bold design thanking international clientele

Design could incorporate fish, knives, fire, wine, wood

No palm trees, coconuts, surfboards,beachballs or tikis
Updates

1. Please show envelope designs that match the card. 

2. Thank you going down the left side of the card cover in a column in at least 5 languages: Mahalo, Japanese, Chinese, French, Spanish, German, Italian

Target Market(s)

Company based on Oahu servicing locals and visitors

Industry/Entity Type

Catering

```html
<!DOCTYPE html>
<html lang="en">
<head>
<meta charset="utf-8">
<title>Moments Catering – Thank You Card</title>
<link rel="stylesheet" href="https://fonts.googleapis.com/css2?family=Cormorant+Garamond:wght@500&family=Parisienne&family=Noto+Serif+JP:wght@400&family=Open+Sans:wght@400&display=swap">
<style>
  :root {
    --page: #ffffff;
    --card-red: #e8331c;
    --card-red-light: #f0482a;
    --card-red-deep: #d72a16;
    --cream: #fbe6b8;
    --inside-type: #fde3cf;
    --photo-light: #f6c8c0;
    --photo-deep: #e06a5a;
    --ink: #111111;
    --fold: #333333;
  }
  html, body {
    margin: 0;
    padding: 0;
    width: 1200px;
    height: 1198px;
    overflow: hidden;
    background: var(--page);
  }
  .sheet {
    display: block;
    width: 1200px;
    height: 1198px;
  }
  .panel-label {
    font-family: "Open Sans", Arial, sans-serif;
    font-size: 15px;
    fill: var(--ink);
  }
  .fold-label {
    font-family: "Open Sans", Arial, sans-serif;
    font-size: 11px;
    fill: var(--ink);
  }
  .fold-line {
    stroke: var(--fold);
    stroke-width: 1.6;
    stroke-dasharray: 4 3;
  }
  .card-paper { fill: url(#redPaper); }
  .card-white { fill: #ffffff; stroke: #d8d8d8; stroke-width: 1; }
  .brand-name {
    font-family: "Cormorant Garamond", Georgia, serif;
    font-style: normal;
    font-weight: 500;
    font-size: 44px;
    letter-spacing: 8px;
    fill: var(--cream);
  }
  .script-thanks {
    font-family: "Parisienne", cursive;
    fill: var(--cream);
  }
  .inside-thanks {
    font-family: "Parisienne", cursive;
    font-size: 24px;
    fill: var(--inside-type);
  }
  .inside-thanks-cjk {
    font-family: "Noto Serif JP", serif;
    font-size: 16px;
    fill: var(--inside-type);
  }
  .message-hint {
    font-family: "Open Sans", Arial, sans-serif;
    font-size: 12px;
    fill: var(--ink);
  }
  .cake-sketch { fill: var(--cream); opacity: 0.55; }
  .shadowed { filter: url(#cardShadow); }
</style>
</head>
<body>
<svg class="sheet" viewBox="0 0 1200 1198" xmlns="http://www.w3.org/2000/svg">
  <defs>
    <linearGradient id="redPaper" x1="0" y1="0" x2="1" y2="1">
      <stop offset="0" stop-color="var(--card-red-light)"/>
      <stop offset="0.5" stop-color="var(--card-red)"/>
      <stop offset="1" stop-color="var(--card-red-deep)"/>
    </linearGradient>
    <linearGradient id="teamPhoto" x1="0" y1="0" x2="0" y2="1">
      <stop offset="0" stop-color="var(--photo-light)"/>
      <stop offset="1" stop-color="var(--photo-deep)"/>
    </linearGradient>
    <filter id="cardShadow" x="-5%" y="-5%" width="112%" height="112%">
      <feDropShadow dx="2" dy="3" stdDeviation="2.5" flood-color="#000" flood-opacity="0.35"/>
    </filter>
  </defs>

  <g class="front-unfolded">
    <text class="panel-label" x="317" y="108" text-anchor="middle">Front of card</text>
    <path class="card-paper" d="M224 147 L360 147 L490 335 L490 768 L146 768 L146 335 Z"/>
    <g transform="rotate(180 324 284)">
      <text class="script-thanks" x="324" y="296" font-size="36" text-anchor="middle">Thank You</text>
    </g>
    <rect class="cake-sketch" x="284" y="176" width="44" height="34" rx="6" role="img" aria-label="Sketch of a slice of cake with a fork"/>
    <text class="brand-name" x="322" y="459" text-anchor="middle">MOMENTS</text>
    <line class="fold-line" x1="108" y1="334" x2="492" y2="334"/>
    <line class="fold-line" x1="108" y1="555" x2="492" y2="555"/>
    <text class="fold-label" x="54" y="337">Fold line</text>
    <text class="fold-label" x="53" y="559">Fold line</text>
  </g>

  <g class="inside-unfolded">
    <text class="panel-label" x="972" y="113" text-anchor="middle">Inside of card</text>
    <path class="card-paper" d="M882 147 L1056 147 L1135 330 L806 330 Z"/>
    <text class="inside-thanks" x="970" y="204" text-anchor="middle">Mahalo</text>
    <text class="inside-thanks-cjk" x="970" y="232" text-anchor="middle">感謝の意</text>
    <text x="970" y="262" text-anchor="middle"><tspan class="inside-thanks-cjk">三江源 </tspan><tspan class="inside-thanks">Merci</tspan></text>
    <text class="inside-thanks" x="970" y="296" text-anchor="middle">Grazie Danke Gracias</text>
    <rect x="806" y="330" width="329" height="180" fill="url(#teamPhoto)" role="img" aria-label="Photo of the catering team in their kitchen"/>
    <rect class="card-white" x="806" y="510" width="329" height="252"/>
    <text class="message-hint" x="970" y="657" text-anchor="middle">Area to write messages</text>
    <line class="fold-line" x1="786" y1="551" x2="1152" y2="551"/>
    <text class="fold-label" x="711" y="555">Fold line</text>
  </g>

  <g class="folded-card shadowed">
    <rect class="card-paper" x="138" y="919" width="336" height="217"/>
    <text class="brand-name" x="310" y="1042" text-anchor="middle">MOMENTS</text>
  </g>

  <g class="envelope-back">
    <rect class="card-paper shadowed" x="803" y="917" width="337" height="227"/>
    <path d="M803 917 L912 1110 L1031 1110 L1140 917" fill="none" stroke="var(--card-red-deep)" stroke-width="2" opacity="0.8"/>
    <text class="script-thanks" x="972" y="992" font-size="46" text-anchor="middle">Thank You</text>
    <rect class="cake-sketch" x="940" y="1022" width="60" height="44" rx="8" role="img" aria-label="Sketch of a slice of cake with a fork"/>
  </g>
</svg>
</body>
</html>
```